Book cover design for the book titled "Beneath the Undertow."

create a book cover. The book title is, "Beneath the Undertow: Why Early Wounds Keep Sinking Our Kind." The purpose of the book is to create awareness of how childhood trauma is impacting 7 out of 10 adults in the world today and that two-thirds of children will experience neglect and or abuse before their 18th birthday. One victim described that his mental and physical illness resulting from childhood trauma felt like he wa being pulled to the ground, that the force was "beneath the undertow." The design should be clean and simple and communicate a crisis.

```html
<!DOCTYPE html>
<html lang="en">
<head>
<meta charset="utf-8">
<title>Beneath the Undertow — Book Cover</title>
<link href="https://fonts.googleapis.com/css2?family=Libre+Baskerville:wght@400;700&display=swap" rel="stylesheet">
<style>
  :root {
    --backdrop: #7aa3ba;
    --navy: #1c2250;
    --night: #151a42;
    --teal: #1f6f8a;
    --aqua: #3fb6b8;
    --peach: #f4c2a8;
    --coral: #f08a6c;
    --glow: #fde6d6;
    --band: rgba(14, 18, 46, 0.85);
  }
  * { margin: 0; padding: 0; box-sizing: border-box; }
  html, body {
    width: 1200px;
    height: 1200px;
    overflow: hidden;
    background: var(--backdrop);
  }
  .canvas {
    position: relative;
    width: 1200px;
    height: 1200px;
    display: flex;
    align-items: center;
    justify-content: center;
  }
  .cover {
    position: relative;
    width: 840px;
    height: 1120px;
    background: var(--navy);
    overflow: hidden;
  }
  .cover-art {
    position: absolute;
    inset: 0;
    background:
      radial-gradient(circle at 50% 40%, var(--glow) 0, #f7cdb4 110px, rgba(244,160,130,0.75) 170px, rgba(63,182,184,0.35) 300px, transparent 420px),
      radial-gradient(ellipse 80% 30% at 50% 62%, rgba(240,138,108,0.55), transparent 70%),
      linear-gradient(to bottom, var(--night) 0%, var(--navy) 28%, #27407a 55%, var(--teal) 78%, #1a3f72 100%);
  }
  .title-block {
    position: absolute;
    top: 110px;
    left: 0;
    right: 0;
    text-align: center;
    font-family: "Libre Baskerville", Georgia, serif;
    color: var(--peach);
  }
  .title {
    display: inline-block;
    padding: 6px 28px 10px;
    background: var(--band);
    font-weight: 700;
    font-size: 68px;
    line-height: 1.05;
    letter-spacing: 1px;
    text-transform: uppercase;
  }
  .subtitle {
    display: inline-block;
    margin-top: 4px;
    padding: 6px 24px;
    background: var(--band);
    font-weight: 700;
    font-size: 22px;
    line-height: 1.15;
  }
</style>
</head>
<body>
  <main class="canvas">
    <article class="cover">
      <div class="cover-art" role="img" aria-label="Illustration: a hooded child sitting at the top of a stairway among peach and teal clouds, facing a large glowing moon in a starry night sky, with birds and stylised flowers in the foreground"></div>
      <header class="title-block">
        <h1 class="title">Beneath the<br>Undertow</h1><br>
        <p class="subtitle">Why Early Wounds Keep<br>Sinking Our Kind.</p>
      </header>
    </article>
  </main>
</body>
</html>
```